Automotive eCommerce Business looking for a business card design

Looking for a clean and simple business card design. Our company name is "Harbor Crest Auto" and we are a company specializing in the ecommerce sales of automotive parts, specifically for pick up trucks and large SUVs. Our company colours are red, black, and white.

Feel free to use the logo provided or create a new logo that you seem fit. Looking forward to your creative ideas!

Industry/Entity Type

Automotive

Contact Information for Business Card

We were thinking of a possibly two-sided design featuring just the logo and company name on one side, and personal information on the other side. Single sided designs will be considered as well.

Font styles to use
Serif
Sans Serif
Decorative

Colors
ec1f27
ffffff
000000

Requirements
Must have
• Space for employee's name, title, phone number and email address, along with the company address and website somewhere.

```html
<!DOCTYPE html>
<html lang="en">
<head>
<meta charset="utf-8">
<title>Harbor Crest Auto – Business Card</title>
<link rel="stylesheet" href="https://fonts.googleapis.com/css2?family=Cinzel:wght@400;600&family=Open+Sans:wght@400;600&display=swap">
<style>
  :root {
    --brand-red: #a61e24;
    --card-white: #fbfbfa;
    --card-black: #141516;
    --ink: #1e1e1e;
    --backdrop: #3a302b;
    --light-text: #ecebea;
  }
  * { margin: 0; padding: 0; box-sizing: border-box; }
  html, body { width: 1200px; height: 844px; overflow: hidden; }
  body {
    background: var(--backdrop);
    display: flex;
    align-items: center;
    justify-content: center;
    gap: 48px;
  }
  .card {
    width: 520px;
    height: 300px;
    position: relative;
    box-shadow: 0 10px 28px rgba(0,0,0,0.45);
  }
  .card--front { background: var(--card-white); color: var(--ink); font-family: "Open Sans", sans-serif; }
  .card--back {
    background: var(--card-black);
    display: flex;
    flex-direction: column;
    align-items: center;
    justify-content: center;
    gap: 26px;
  }
  .brand-mark {
    position: absolute;
    top: 56px;
    right: 70px;
    display: flex;
    align-items: center;
    gap: 12px;
  }
  .brand-square { width: 22px; height: 22px; background: var(--brand-red); }
  .brand-name {
    font-family: "Cinzel", serif;
    font-weight: 600;
    font-size: 22px;
    color: var(--brand-red);
    letter-spacing: 0.5px;
  }
  .contact {
    position: absolute;
    left: 32px;
    bottom: 28px;
    font-size: 12.5px;
    line-height: 1.5;
  }
  .contact__name { color: var(--brand-red); font-weight: 600; font-size: 16px; line-height: 1.2; }
  .contact__title { margin-bottom: 22px; }
  .contact__address { margin-bottom: 20px; }
  .label { color: var(--brand-red); }
  .web { color: var(--brand-red); margin-left: 10px; }
  .gap { margin-left: 8px; }
  .back-square { width: 70px; height: 70px; background: var(--brand-red); border-radius: 6px; }
  .back-name {
    font-family: "Cinzel", serif;
    font-weight: 400;
    font-size: 30px;
    color: var(--light-text);
    letter-spacing: 1px;
  }
</style>
</head>
<body>
  <section class="card card--front" aria-label="Business card front">
    <div class="brand-mark">
      <span class="brand-square"></span>
      <span class="brand-name">Harbor Crest Auto</span>
    </div>
    <div class="contact">
      <p class="contact__name">Daniel Reyes</p>
      <p class="contact__title">Managing Director</p>
      <p class="contact__address">418 Quayside Road, Portland, 04101</p>
      <p><span class="label">T:</span>(207) 555 0148<span class="gap label">F:</span>(207) 555 0149<span class="gap label">M:</span>(207) 5550150</p>
      <p><span class="label">E:</span>parts@harborcrestauto.example<span class="web">www.harborcrestauto.example</span></p>
    </div>
  </section>
  <section class="card card--back" aria-label="Business card back">
    <span class="back-square"></span>
    <p class="back-name">Harbor Crest Auto Ltd</p>
  </section>
</body>
</html>
```